2014 Calendars

We need the four file updated for 2014. It's actually just two designs, the only thing that changes to make it four files is the PH# and text just above the PH#.

We are happy with the layout so really just need the calendars to be updated.

Our colors are:
Teal = Pantone 3272 // C100, M0, Y44, K0 // R0, G170, B166
Grey = Pantone 7540 // C0, M0, Y0, K72, // R105, G106, B109

```html
<!DOCTYPE html>
<html lang="en">
<head>
<meta charset="utf-8">
<title>2014 Calendar – MoveWell</title>
<link rel="stylesheet" href="https://fonts.googleapis.com/css2?family=Roboto+Condensed:wght@400;700&family=Raleway:ital,wght@0,200;0,500;1,400&display=swap">
<style>
  :root {
    --teal: #00aaa6;
    --teal-light: #7dcfcc;
    --grey: #696a6d;
    --ink: #111111;
    --white: #ffffff;
  }
  * { box-sizing: border-box; margin: 0; padding: 0; }
  html, body { width: 1200px; height: 1000px; overflow: hidden; background: var(--white); }
  .sheet { position: relative; width: 1200px; height: 1000px; overflow: hidden; }

  .calendar-band {
    position: absolute; left: 0; top: 0; width: 1200px; height: 703px;
    background: var(--teal);
  }
  .year-mark {
    position: absolute; left: 1054px; top: 357px;
    transform: translate(-50%, -50%) rotate(90deg);
    font-family: "Raleway", sans-serif; font-weight: 200;
    font-size: 232px; line-height: 1; letter-spacing: 8px;
    color: var(--teal-light); white-space: nowrap;
  }
  .month {
    position: absolute; width: 205px; height: 180px;
    background: var(--white); color: var(--ink);
    font-family: "Roboto Condensed", sans-serif;
    padding-top: 7px; z-index: 1;
  }
  .col-1 { left: 61px; } .col-2 { left: 295px; } .col-3 { left: 529px; } .col-4 { left: 763px; }
  .row-1 { top: 54px; } .row-2 { top: 266px; } .row-3 { top: 480px; }
  .month-name { text-align: center; font-weight: 700; font-size: 16px; line-height: 17px; }
  .weekdays, .days {
    display: grid; grid-template-columns: repeat(7, 23.5px);
    width: 164.5px; margin: 0 auto; text-align: center;
    font-size: 15px; line-height: 19.3px;
  }
  .weekdays { font-weight: 700; }
  .days span:first-child { grid-column-start: var(--start); }
  .start-sun { --start: 1; } .start-mon { --start: 2; } .start-tue { --start: 3; }
  .start-wed { --start: 4; } .start-thu { --start: 5; } .start-fri { --start: 6; } .start-sat { --start: 7; }

  .brand { position: absolute; left: 84px; top: 770px; }
  .brand-name {
    font-family: "Raleway", sans-serif; font-weight: 500;
    font-size: 104px; line-height: 1; letter-spacing: -2px; color: var(--grey);
  }
  .brand-tagline {
    margin-top: 14px; font-family: "Raleway", sans-serif; font-weight: 500;
    font-size: 21px; color: var(--teal); letter-spacing: 0.3px;
  }
  .contact { position: absolute; left: 654px; top: 786px; width: 470px; }
  .contact-line {
    font-family: "Raleway", sans-serif; font-style: italic; font-weight: 400;
    font-size: 26px; color: var(--grey); white-space: nowrap;
  }
  .contact-phone {
    margin-top: 2px; font-family: "Roboto Condensed", sans-serif; font-weight: 700;
    font-size: 92px; line-height: 1; color: var(--teal); letter-spacing: -1px;
  }
</style>
</head>
<body>
<main class="sheet">
  <section class="calendar-band" aria-label="2014 calendar">
    <div class="year-mark" aria-hidden="true">2014</div>

    <article class="month col-1 row-1"><h2 class="month-name">January</h2>
      <div class="weekdays"><span>S</span><span>M</span><span>T</span><span>W</span><span>T</span><span>F</span><span>S</span></div>
      <div class="days start-wed"><span>1</span><span>2</span><span>3</span><span>4</span><span>5</span><span>6</span><span>7</span><span>8</span><span>9</span><span>10</span><span>11</span><span>12</span><span>13</span><span>14</span><span>15</span><span>16</span><span>17</span><span>18</span><span>19</span><span>20</span><span>21</span><span>22</span><span>23</span><span>24</span><span>25</span><span>26</span><span>27</span><span>28</span><span>29</span><span>30</span><span>31</span></div>
    </article>

    <article class="month col-2 row-1"><h2 class="month-name">February</h2>
      <div class="weekdays"><span>S</span><span>M</span><span>T</span><span>W</span><span>T</span><span>F</span><span>S</span></div>
      <div class="days start-sat"><span>1</span><span>2</span><span>3</span><span>4</span><span>5</span><span>6</span><span>7</span><span>8</span><span>9</span><span>10</span><span>11</span><span>12</span><span>13</span><span>14</span><span>15</span><span>16</span><span>17</span><span>18</span><span>19</span><span>20</span><span>21</span><span>22</span><span>23</span><span>24</span><span>25</span><span>26</span><span>27</span><span>28</span></div>
    </article>

    <article class="month col-3 row-1"><h2 class="month-name">March</h2>
      <div class="weekdays"><span>S</span><span>M</span><span>T</span><span>W</span><span>T</span><span>F</span><span>S</span></div>
      <div class="days start-sat"><span>1</span><span>2</span><span>3</span><span>4</span><span>5</span><span>6</span><span>7</span><span>8</span><span>9</span><span>10</span><span>11</span><span>12</span><span>13</span><span>14</span><span>15</span><span>16</span><span>17</span><span>18</span><span>19</span><span>20</span><span>21</span><span>22</span><span>23</span><span>24</span><span>25</span><span>26</span><span>27</span><span>28</span><span>29</span><span>30</span><span>31</span></div>
    </article>

    <article class="month col-4 row-1"><h2 class="month-name">April</h2>
      <div class="weekdays"><span>S</span><span>M</span><span>T</span><span>W</span><span>T</span><span>F</span><span>S</span></div>
      <div class="days start-tue"><span>1</span><span>2</span><span>3</span><span>4</span><span>5</span><span>6</span><span>7</span><span>8</span><span>9</span><span>10</span><span>11</span><span>12</span><span>13</span><span>14</span><span>15</span><span>16</span><span>17</span><span>18</span><span>19</span><span>20</span><span>21</span><span>22</span><span>23</span><span>24</span><span>25</span><span>26</span><span>27</span><span>28</span><span>29</span><span>30</span></div>
    </article>

    <article class="month col-1 row-2"><h2 class="month-name">May</h2>
      <div class="weekdays"><span>S</span><span>M</span><span>T</span><span>W</span><span>T</span><span>F</span><span>S</span></div>
      <div class="days start-thu"><span>1</span><span>2</span><span>3</span><span>4</span><span>5</span><span>6</span><span>7</span><span>8</span><span>9</span><span>10</span><span>11</span><span>12</span><span>13</span><span>14</span><span>15</span><span>16</span><span>17</span><span>18</span><span>19</span><span>20</span><span>21</span><span>22</span><span>23</span><span>24</span><span>25</span><span>26</span><span>27</span><span>28</span><span>29</span><span>30</span><span>31</span></div>
    </article>

    <article class="month col-2 row-2"><h2 class="month-name">June</h2>
      <div class="weekdays"><span>S</span><span>M</span><span>T</span><span>W</span><span>T</span><span>F</span><span>S</span></div>
      <div class="days start-sun"><span>1</span><span>2</span><span>3</span><span>4</span><span>5</span><span>6</span><span>7</span><span>8</span><span>9</span><span>10</span><span>11</span><span>12</span><span>13</span><span>14</span><span>15</span><span>16</span><span>17</span><span>18</span><span>19</span><span>20</span><span>21</span><span>22</span><span>23</span><span>24</span><span>25</span><span>26</span><span>27</span><span>28</span><span>29</span><span>30</span></div>
    </article>

    <article class="month col-3 row-2"><h2 class="month-name">July</h2>
      <div class="weekdays"><span>S</span><span>M</span><span>T</span><span>W</span><span>T</span><span>F</span><span>S</span></div>
      <div class="days start-tue"><span>1</span><span>2</span><span>3</span><span>4</span><span>5</span><span>6</span><span>7</span><span>8</span><span>9</span><span>10</span><span>11</span><span>12</span><span>13</span><span>14</span><span>15</span><span>16</span><span>17</span><span>18</span><span>19</span><span>20</span><span>21</span><span>22</span><span>23</span><span>24</span><span>25</span><span>26</span><span>27</span><span>28</span><span>29</span><span>30</span><span>31</span></div>
    </article>

    <article class="month col-4 row-2"><h2 class="month-name">August</h2>
      <div class="weekdays"><span>S</span><span>M</span><span>T</span><span>W</span><span>T</span><span>F</span><span>S</span></div>
      <div class="days start-fri"><span>1</span><span>2</span><span>3</span><span>4</span><span>5</span><span>6</span><span>7</span><span>8</span><span>9</span><span>10</span><span>11</span><span>12</span><span>13</span><span>14</span><span>15</span><span>16</span><span>17</span><span>18</span><span>19</span><span>20</span><span>21</span><span>22</span><span>23</span><span>24</span><span>25</span><span>26</span><span>27</span><span>28</span><span>29</span><span>30</span><span>31</span></div>
    </article>

    <article class="month col-1 row-3"><h2 class="month-name">September</h2>
      <div class="weekdays"><span>S</span><span>M</span><span>T</span><span>W</span><span>T</span><span>F</span><span>S</span></div>
      <div class="days start-mon"><span>1</span><span>2</span><span>3</span><span>4</span><span>5</span><span>6</span><span>7</span><span>8</span><span>9</span><span>10</span><span>11</span><span>12</span><span>13</span><span>14</span><span>15</span><span>16</span><span>17</span><span>18</span><span>19</span><span>20</span><span>21</span><span>22</span><span>23</span><span>24</span><span>25</span><span>26</span><span>27</span><span>28</span><span>29</span><span>30</span></div>
    </article>

    <article class="month col-2 row-3"><h2 class="month-name">October</h2>
      <div class="weekdays"><span>S</span><span>M</span><span>T</span><span>W</span><span>T</span><span>F</span><span>S</span></div>
      <div class="days start-wed"><span>1</span><span>2</span><span>3</span><span>4</span><span>5</span><span>6</span><span>7</span><span>8</span><span>9</span><span>10</span><span>11</span><span>12</span><span>13</span><span>14</span><span>15</span><span>16</span><span>17</span><span>18</span><span>19</span><span>20</span><span>21</span><span>22</span><span>23</span><span>24</span><span>25</span><span>26</span><span>27</span><span>28</span><span>29</span><span>30</span><span>31</span></div>
    </article>

    <article class="month col-3 row-3"><h2 class="month-name">November</h2>
      <div class="weekdays"><span>S</span><span>M</span><span>T</span><span>W</span><span>T</span><span>F</span><span>S</span></div>
      <div class="days start-sat"><span>1</span><span>2</span><span>3</span><span>4</span><span>5</span><span>6</span><span>7</span><span>8</span><span>9</span><span>10</span><span>11</span><span>12</span><span>13</span><span>14</span><span>15</span><span>16</span><span>17</span><span>18</span><span>19</span><span>20</span><span>21</span><span>22</span><span>23</span><span>24</span><span>25</span><span>26</span><span>27</span><span>28</span><span>29</span><span>30</span></div>
    </article>

    <article class="month col-4 row-3"><h2 class="month-name">December</h2>
      <div class="weekdays"><span>S</span><span>M</span><span>T</span><span>W</span><span>T</span><span>F</span><span>S</span></div>
      <div class="days start-mon"><span>1</span><span>2</span><span>3</span><span>4</span><span>5</span><span>6</span><span>7</span><span>8</span><span>9</span><span>10</span><span>11</span><span>12</span><span>13</span><span>14</span><span>15</span><span>16</span><span>17</span><span>18</span><span>19</span><span>20</span><span>21</span><span>22</span><span>23</span><span>24</span><span>25</span><span>26</span><span>27</span><span>28</span><span>29</span><span>30</span><span>31</span></div>
    </article>
  </section>

  <footer>
    <div class="brand">
      <div class="brand-name">MoveWell</div>
      <div class="brand-tagline">Your Medical Supply Advocate</div>
    </div>
    <div class="contact">
      <p class="contact-line">Committed to making your life easier</p>
      <p class="contact-phone">800.555.0147</p>
    </div>
  </footer>
</main>
</body>
</html>
```